HVAC Door Hanger- 4.25 inches by 11 inches

Hello We are using the Brightwell door hanger as an inspiration for our new door hanger. The company name is Harborline Home Services. Logo files attached. The Slogan needs to be added on the front with the Logo "Southern California’s Trusted Name in Home Services". Instead of the X protection plan, the name will be Full Shield by Harborline or Harborline Climate Keeper- The slogan for this package will be "Peace of Mind, For Every Season

```html
<!DOCTYPE html>
<html lang="en">
<head>
<meta charset="utf-8">
<title>Harborline Home Services – Door Hangers</title>
<link href="https://fonts.googleapis.com/css2?family=Anton&family=Montserrat:wght@700;800&family=Oswald:wght@400;500;600;700&display=swap" rel="stylesheet">
<style>
  :root{
    --bg:#6b7a7b;
    --blue:#2a84d2;
    --red:#f50a0a;
    --orange:#f7901e;
    --yellow:#eef21a;
    --white:#ffffff;
    --ink:#111111;
    --photo-a:#c9ccce;
    --photo-b:#3d6fb8;
  }
  *{margin:0;padding:0;box-sizing:border-box}
  html,body{width:1200px;height:1200px;overflow:hidden;background:var(--bg)}
  .canvas{position:relative;width:1200px;height:1200px}
  .hanger{position:absolute;top:95px;width:391px;height:1010px;overflow:hidden}
  .hanger--front{left:192px}
  .hanger--back{left:618px}
  .hanger__art{position:absolute;inset:0;width:391px;height:1010px}
  .abs{position:absolute}

  /* brand */
  .brand-name{left:32px;top:168px;font:800 37px/1 'Montserrat',sans-serif;color:var(--blue);letter-spacing:.5px}
  .brand-sub{left:34px;top:208px;font:800 12px/1 'Montserrat',sans-serif;color:var(--blue);letter-spacing:10.4px}
  .brand-mark{left:326px;top:172px;width:30px;height:30px;background:var(--orange)}
  .brand-trades{left:32px;top:229px;font:700 10.6px/1 'Montserrat',sans-serif;color:var(--red);letter-spacing:1.6px;white-space:nowrap}

  /* front headline */
  .headline{left:30px;width:340px;text-align:center;font-family:'Anton',sans-serif;color:var(--white);line-height:1;white-space:nowrap}
  .headline--1{top:698px;font-size:76px;letter-spacing:1px}
  .headline--2{top:770px;font-size:66px;letter-spacing:.5px}
  .headline-sub{left:30px;top:840px;width:340px;text-align:center;font:500 23.5px/1 'Oswald',sans-serif;color:var(--white);white-space:nowrap}

  /* footer */
  .phone{left:72px;top:894px;font:600 46px/1 'Oswald',sans-serif;color:var(--white);white-space:nowrap;letter-spacing:.3px}
  .phone-icon{left:20px;top:900px;width:42px;height:42px}
  .url{left:0;width:391px;top:964px;text-align:center;font:600 24px/1 'Oswald',sans-serif;color:var(--ink);white-space:nowrap}

  /* back */
  .plan-title{left:40px;top:190px;width:250px;text-align:center;font:600 31px/34.5px 'Oswald',sans-serif;color:var(--white);text-transform:uppercase}
  .plan-price{left:20px;top:302px;width:302px;text-align:center;font:600 25px/1 'Oswald',sans-serif;color:var(--white);white-space:nowrap}
  .coupon-side{left:38px;top:395px;width:82px;height:112px;display:flex;align-items:center;justify-content:center}
  .coupon-side span{transform:rotate(-90deg);font:700 24px/24px 'Oswald',sans-serif;color:var(--white);text-align:center;white-space:nowrap}
  .coupon-kicker{left:147px;top:357px;font:800 13px/1 'Montserrat',sans-serif;color:var(--blue);white-space:nowrap}
  .coupon-deal{left:146px;top:375px;font:400 42px/1 'Anton',sans-serif;color:var(--red);white-space:nowrap}
  .coupon-list{left:158px;top:433px;list-style:none;font:400 8.6px/12px 'Oswald',sans-serif;color:var(--ink)}
  .coupon-list li{position:relative;padding-left:11px;white-space:nowrap}
  .coupon-list li::before{content:"";position:absolute;left:0;top:3px;width:6px;height:6px;border-radius:50%;background:var(--red)}
  .offer{left:20px;top:516px;width:302px;text-align:center;font:700 38px/1 'Oswald',sans-serif;color:var(--yellow);white-space:nowrap}
  .season{left:43px;top:603px;font:600 24.5px/1 'Oswald',sans-serif;color:var(--white);white-space:nowrap}
  .season-list{left:40px;top:643px;width:318px;list-style:none;font:400 15.2px/18px 'Oswald',sans-serif;color:var(--white)}
  .season-list li{position:relative;padding-left:22px;margin-bottom:8px}
  .season-list li svg{position:absolute;left:0;top:5px;width:11px;height:11px}
</style>
</head>
<body>
<main class="canvas">

  <!-- FRONT -->
  <section class="hanger hanger--front">
    <svg class="hanger__art" viewBox="0 0 629 1626" preserveAspectRatio="none">
      <defs>
        <linearGradient id="photoTone" x1="0" y1="0" x2="1" y2="1">
          <stop offset="0" stop-color="var(--photo-a)"/>
          <stop offset=".6" stop-color="#8b8f94"/>
          <stop offset="1" stop-color="var(--photo-b)"/>
        </linearGradient>
      </defs>
      <rect width="629" height="1626" fill="var(--white)"/>
      <g role="img" aria-label="Photo: technician in a blue hard hat and gloves adjusting a heating manifold with a wrench">
        <polygon points="0,657 251,414 629,742 629,1102 0,1102" fill="url(#photoTone)"/>
      </g>
      <rect x="36" y="512" width="64" height="16" rx="8" fill="var(--orange)"/>
      <rect x="556" y="744" width="73" height="196" fill="var(--white)"/>
      <rect x="579" y="767" width="25" height="140" fill="var(--orange)"/>
      <rect x="556" y="940" width="73" height="162" fill="var(--red)"/>
      <rect x="29" y="1102" width="600" height="308" fill="var(--red)"/>
      <rect y="1424" width="629" height="116" fill="var(--blue)"/>
      <rect y="1540" width="629" height="86" fill="var(--orange)"/>
      <rect x="34" y="1612" width="563" height="14" fill="var(--white)"/>
      <circle cx="314" cy="160" r="84" fill="var(--bg)"/>
    </svg>

    <div class="abs brand-name">HARBORLINE</div>
    <div class="abs brand-mark"></div>
    <div class="abs brand-sub">HOME SERVICES</div>
    <div class="abs brand-trades">HEATING COOLING PLUMBING ELECTRICAL</div>

    <div class="abs headline headline--1">SOUTHERN</div>
    <div class="abs headline headline--2">CALIFORNIA’S</div>
    <div class="abs headline-sub">TRUSTED NAME IN HOME SERVICES</div>

    <svg class="abs phone-icon" viewBox="0 0 42 42" aria-hidden="true">
      <circle cx="21" cy="21" r="20" fill="var(--red)" stroke="var(--white)" stroke-width="1.5"/>
      <rect x="15" y="10" width="12" height="21" rx="2" fill="none" stroke="var(--white)" stroke-width="2"/>
      <line x1="19" y1="27" x2="23" y2="27" stroke="var(--white)" stroke-width="2"/>
    </svg>
    <div class="abs phone">0655 (412) 380</div>
    <div class="abs url">www.harborlinehomeservices.com</div>
  </section>

  <!-- BACK -->
  <section class="hanger hanger--back">
    <svg class="hanger__art" viewBox="0 0 629 1626" preserveAspectRatio="none">
      <rect width="629" height="1626" fill="var(--white)"/>
      <circle cx="629" cy="310" r="125" fill="var(--orange)"/>
      <rect x="28" y="772" width="601" height="633" fill="var(--red)"/>
      <rect x="556" y="577" width="73" height="195" fill="var(--white)"/>
      <rect x="580" y="602" width="25" height="138" fill="var(--orange)"/>
      <rect x="40" y="357" width="60" height="135" fill="var(--blue)"/>
      <rect x="38" y="342" width="62" height="20" rx="10" fill="var(--orange)"/>
      <polygon points="0,492 250,245 627,574 556,574 556,927 0,927" fill="var(--blue)"/>
      <!-- coupon -->
      <rect x="32" y="564" width="483" height="251" fill="var(--white)"/>
      <rect x="32" y="564" width="174" height="251" fill="var(--orange)"/>
      <rect x="62" y="592" width="128" height="198" fill="none" stroke="var(--white)" stroke-width="2" stroke-dasharray="6 5"/>
      <rect x="238" y="693" width="239" height="97" fill="none" stroke="var(--blue)" stroke-width="2" stroke-dasharray="6 5"/>
      <g fill="var(--blue)">
        <circle cx="32" cy="690" r="13"/><circle cx="515" cy="690" r="13"/>
        <circle cx="46" cy="564" r="4.5"/><circle cx="62" cy="564" r="4.5"/><circle cx="78" cy="564" r="4.5"/><circle cx="94" cy="564" r="4.5"/><circle cx="110" cy="564" r="4.5"/><circle cx="126" cy="564" r="4.5"/><circle cx="142" cy="564" r="4.5"/><circle cx="158" cy="564" r="4.5"/><circle cx="174" cy="564" r="4.5"/><circle cx="190" cy="564" r="4.5"/><circle cx="222" cy="564" r="4.5"/><circle cx="238" cy="564" r="4.5"/><circle cx="254" cy="564" r="4.5"/><circle cx="270" cy="564" r="4.5"/><circle cx="286" cy="564" r="4.5"/><circle cx="302" cy="564" r="4.5"/><circle cx="318" cy="564" r="4.5"/><circle cx="334" cy="564" r="4.5"/><circle cx="350" cy="564" r="4.5"/><circle cx="366" cy="564" r="4.5"/><circle cx="382" cy="564" r="4.5"/><circle cx="398" cy="564" r="4.5"/><circle cx="414" cy="564" r="4.5"/><circle cx="430" cy="564" r="4.5"/><circle cx="446" cy="564" r="4.5"/><circle cx="462" cy="564" r="4.5"/><circle cx="478" cy="564" r="4.5"/><circle cx="494" cy="564" r="4.5"/>
        <circle cx="46" cy="815" r="4.5"/><circle cx="62" cy="815" r="4.5"/><circle cx="78" cy="815" r="4.5"/><circle cx="94" cy="815" r="4.5"/><circle cx="110" cy="815" r="4.5"/><circle cx="126" cy="815" r="4.5"/><circle cx="142" cy="815" r="4.5"/><circle cx="158" cy="815" r="4.5"/><circle cx="174" cy="815" r="4.5"/><circle cx="190" cy="815" r="4.5"/><circle cx="222" cy="815" r="4.5"/><circle cx="238" cy="815" r="4.5"/><circle cx="254" cy="815" r="4.5"/><circle cx="270" cy="815" r="4.5"/><circle cx="286" cy="815" r="4.5"/><circle cx="302" cy="815" r="4.5"/><circle cx="318" cy="815" r="4.5"/><circle cx="334" cy="815" r="4.5"/><circle cx="350" cy="815" r="4.5"/><circle cx="366" cy="815" r="4.5"/><circle cx="382" cy="815" r="4.5"/><circle cx="398" cy="815" r="4.5"/><circle cx="414" cy="815" r="4.5"/><circle cx="430" cy="815" r="4.5"/><circle cx="446" cy="815" r="4.5"/><circle cx="462" cy="815" r="4.5"/><circle cx="478" cy="815" r="4.5"/><circle cx="494" cy="815" r="4.5"/>
      </g>
      <rect y="1424" width="629" height="116" fill="var(--blue)"/>
      <rect y="1540" width="629" height="86" fill="var(--orange)"/>
      <rect x="34" y="1612" width="563" height="14" fill="var(--white)"/>
      <circle cx="314" cy="160" r="84" fill="var(--bg)"/>
    </svg>

    <div class="abs plan-title">Full<br>Shield by<br>Harborline</div>
    <div class="abs plan-price">$XXX/MONTH TO $XXX/MONTH</div>

    <div class="abs coupon-side"><span>DISCOUNT<br>COUPON</span></div>
    <div class="abs coupon-kicker">VOUCHER SHOPPING</div>
    <div class="abs coupon-deal">75% OFF</div>
    <ul class="abs coupon-list">
      <li>It is a long established fact that a</li>
      <li>Make a type specimen book</li>
      <li>Westbrook College in Vermont</li>
      <li>There are many variations</li>
    </ul>
    <div class="abs offer">LIMITED TIME OFFER!</div>

    <div class="abs season">Peace of Mind, For Every Season</div>
    <ul class="abs season-list">
      <li><svg viewBox="0 0 12 12" aria-hidden="true"><circle cx="6" cy="6" r="5" fill="none" stroke="#fff" stroke-width="1"/><path d="M3.5 6.2l1.8 1.7 3.3-3.6" fill="none" stroke="#fff" stroke-width="1.2"/></svg>Sed ut perspiciatis unde omnis iste natus error sit accusantium doloremque laudantium,</li>
      <li><svg viewBox="0 0 12 12" aria-hidden="true"><circle cx="6" cy="6" r="5" fill="none" stroke="#fff" stroke-width="1"/><path d="M3.5 6.2l1.8 1.7 3.3-3.6" fill="none" stroke="#fff" stroke-width="1.2"/></svg>But I must explain to you how all this mistaken idea pleasure and praising pain was born and I will account of the system, and expound the actual of the great explorer of the truth,</li>
      <li><svg viewBox="0 0 12 12" aria-hidden="true"><circle cx="6" cy="6" r="5" fill="none" stroke="#fff" stroke-width="1"/><path d="M3.5 6.2l1.8 1.7 3.3-3.6" fill="none" stroke="#fff" stroke-width="1.2"/></svg>On the other hand, we denounce with righteous dislike men who are</li>
      <li><svg viewBox="0 0 12 12" aria-hidden="true"><circle cx="6" cy="6" r="5" fill="none" stroke="#fff" stroke-width="1"/><path d="M3.5 6.2l1.8 1.7 3.3-3.6" fill="none" stroke="#fff" stroke-width="1.2"/></svg>Praising pain was born and I will give you a complete the system, and expound the actual teachings</li>
    </ul>

    <svg class="abs phone-icon" viewBox="0 0 42 42" aria-hidden="true">
      <circle cx="21" cy="21" r="20" fill="var(--red)" stroke="var(--white)" stroke-width="1.5"/>
      <rect x="15" y="10" width="12" height="21" rx="2" fill="none" stroke="var(--white)" stroke-width="2"/>
      <line x1="19" y1="27" x2="23" y2="27" stroke="var(--white)" stroke-width="2"/>
    </svg>
    <div class="abs phone">0655 (412) 380</div>
    <div class="abs url">www.harborlinehomeservices.com</div>
  </section>

</main>
</body>
</html>
```